Glossaro: Graphic elements & webpage layout

Hi there! We’re building a site called Glossaro.com—it will be a community site for beauty product reviews, product recommendations and beauty tutorials. We've already got a logo, thanks to another ArtHively project. This project on ArtHively involves the following web design work:

1) Propose the overall graphic design elements of our site (according to our guidelines, which are in the attached file)

-Color Palette
-Fonts
-Icon set(s)

2) Using the overall graphic design elements in step 1 and our storyboard (attached), develop a webpage layout for the "How-to" page of our site. The "How-to" pages will be an editorial format, where our beauty journalist will show a video (and photos) of step-by-step beauty tutorials.

Please take a look at the attached files for a detailed brief and the logo! Thanks and we're looking forward to working with you!

Target Market(s)

Glossaro is for a French, English, and American audience of women between the ages of 16 and 30, who buy and use beauty products regularly.

Industry/Entity Type

Graphic Design

Requirements
Must have
• 1) A global set of graphic standards for the website Glossaro.com:
• A color palette
• Fonts
• An icon set (or sets)
• A menu
• Other graphic elements like button styles

2) A webpage layout (non-coded) for the How-To page template
(See storyboard, attached separately)
This webpage layout is for the main editorial format on Glossaro—step by step beauty tutorials. The individual on-page elements are in the storyboard, but overall we’d like it to look clean, friendly, and to encourage community participation and sharing on social networks.
Nice to have
• • A look and feel that is fresh, clean and modern
• Proximity: Establishes a close proximity with the user. (We want them to get the same feeling they get when talking beauty tips with their close friends).
• Neutrality: A sincere and neutral look and feel that doesn’t suggest a preference for any particular or elite type of beauty (but it can still be fun!)
• The graphic design is relevant to the beauty sector as a whole. (We could be talking about lipstick, a hairbrush or a man’s cologne)
• The graphic design alludes to the beauty industry (discreetly, not overtly!)
Should not have
• We've already got a logo, so you shouldn't suggest a new one!

We really want to avoid designs that are too traditionally "beauty" or too girly and feminine. Please no pink, no flowers, etc! :)

```html
<!DOCTYPE html>
<html lang="en">
<head>
<meta charset="utf-8">
<title>Glossaro – How To</title>
<link rel="stylesheet" href="https://fonts.googleapis.com/css2?family=Open+Sans:wght@300;400;600;700&family=Arimo:wght@400;700&display=swap">
<style>
:root{
  --teal:#1bbda7;
  --teal-dark:#13a08d;
  --teal-pale:#e6f7f4;
  --orange:#f7921e;
  --orange-dark:#e07a0a;
  --nav:#2a2a2a;
  --ink:#333;
  --muted:#666;
  --line:#cfcfcf;
  --white:#fff;
}
*{box-sizing:border-box;margin:0;padding:0}
html,body{width:1200px;height:2222px;overflow:hidden}
body{position:relative;background:var(--white);font-family:"Arimo",Arial,sans-serif;color:var(--ink);font-size:12px}
.abs{position:absolute}

/* header */
.site-header{left:0;top:0;width:1200px;height:240px;background:linear-gradient(#ececec,#fafafa 60%,#f2f2f2)}
.brand{left:150px;top:58px;display:flex;align-items:center;gap:12px;font-family:"Open Sans",sans-serif;font-weight:700;font-size:58px;color:#222;letter-spacing:-1px}
.brand-dot{width:22px;height:22px;border-radius:50%;background:var(--teal)}
.subscribe{left:772px;top:16px;font-size:12px;color:#444;display:flex;align-items:center;gap:6px}
.subscribe .lead{color:var(--orange-dark)}
.rss{width:14px;height:14px;border-radius:3px;background:var(--orange)}
.search{left:780px;top:56px;width:245px;height:30px;border:1px solid #bbb;border-radius:4px;background:#fff}
.search-btn{left:1030px;top:56px;width:30px;height:30px;border-radius:4px;background:var(--teal)}
.social{top:127px;width:30px;height:30px;border-radius:50%;background:#fff;border:1px solid #ccc;box-shadow:0 1px 2px rgba(0,0,0,.2)}
.social.one{left:640px}.social.two{left:686px}.social.three{left:733px}
.social span{display:block;width:14px;height:14px;border-radius:50%;margin:7px}
.social.one span{background:#3b5b98}.social.two span{background:#33b8e8}.social.three span{background:#f27a1a}
.pill{top:126px;height:32px;border-radius:7px;background:linear-gradient(var(--orange),var(--orange-dark));color:#fff;font-family:"Open Sans",sans-serif;font-weight:700;font-size:15px;display:flex;align-items:center;justify-content:center;letter-spacing:.5px}
.pill.howto{left:780px;width:203px}
.pill.tips{left:1000px;width:62px}

.main-nav{left:141px;top:178px;width:921px;height:54px;border-radius:8px;background:linear-gradient(#3a3a3a,var(--nav));display:flex;align-items:center;padding-left:22px;gap:30px;font-size:12px;color:#fff}
.main-nav a{color:#fff;text-decoration:none;padding:7px 8px}
.main-nav a.active{background:var(--teal);border-radius:3px;color:#fff}

/* feature band */
.band{left:0;top:240px;width:1200px;height:320px;background:var(--teal)}
.feature{left:141px;top:240px;width:921px;height:422px;background:var(--teal);border-radius:0 0 12px 12px}
.feature-title{left:166px;top:252px;font-family:"Open Sans",sans-serif;font-weight:300;font-size:40px;color:#fff}
.meta{left:166px;top:305px;display:flex;gap:38px;font-size:11px;color:#fff}
.meta i{display:inline-block;width:7px;height:7px;border-radius:50%;background:var(--orange);margin-left:2px}
.meta i.off{background:#fff}
.player{left:163px;top:328px;width:442px;height:307px;background:#111;border:3px solid #222}
.video-still{left:0;top:0;width:436px;height:266px;background:linear-gradient(90deg,#cfc9c0 0%,#e6ded2 45%,#b89c86 75%,#6e5849 100%)}
.play{left:196px;top:112px;width:46px;height:42px;border-radius:6px;background:rgba(20,20,20,.8)}
.controls{left:0;top:266px;width:436px;height:35px;background:linear-gradient(#2c2c2c,#0f0f0f);display:flex;align-items:center;gap:10px;padding:0 10px;color:#ddd;font-size:10px}
.track{flex:1;height:4px;background:#555;border-radius:2px}
.track b{display:block;width:18%;height:4px;background:#aaa;border-radius:2px}
.feature-copy{left:627px;top:318px;width:435px;font-size:11px;line-height:17px;color:#fff}
.feature-copy .more{color:#e4fffa;margin-left:4px}
.product-list{left:627px;top:430px;width:410px;list-style:none}
.product-list li{height:44px;border-bottom:1px solid rgba(255,255,255,.45);display:flex;align-items:center;gap:14px;color:#fff}
.product-list .bullet{width:18px;height:18px;border-radius:50%;background:#0f6f62;flex:none}
.product-list strong{display:block;font-size:13px}
.product-list small{font-size:10px;opacity:.9}

/* photo panel */
.tab{top:679px;height:26px;width:92px;border-radius:6px 6px 0 0;color:#fff;font-family:"Open Sans",sans-serif;font-weight:600;font-size:13px;display:flex;align-items:center;justify-content:center}
.tab.video{left:141px;background:var(--orange)}
.tab.photo{left:235px;background:var(--teal)}
.photo-panel{left:141px;top:704px;width:496px;height:506px;background:var(--teal);border-radius:0 10px 10px 10px}
.gallery-photo{left:178px;top:766px;width:415px;height:247px;border:4px solid #222;background:linear-gradient(100deg,#d9d3cc 0%,#c8a58c 35%,#efe7df 60%,#7b6658 100%)}
.arrow{top:872px;width:44px;height:44px;border-radius:50%;background:#1e5e55}
.arrow.prev{left:141px}.arrow.next{left:586px}
.panel-title{left:166px;top:1024px;font-family:"Open Sans",sans-serif;font-weight:300;font-size:38px;color:#fff}
.panel-copy{left:166px;top:1085px;width:450px;font-size:11px;line-height:17px;color:#fff}

/* comment form */
.form-title{left:141px;top:1254px;font-weight:700;font-size:12px;color:var(--teal);letter-spacing:.5px}
.label{left:141px;font-size:12px;color:var(--teal)}
.field{border:1px solid var(--line);background:#fff;border-radius:2px}
.name-field{left:217px;top:1280px;width:420px;height:26px}
.email-field{left:217px;top:1317px;width:253px;height:26px}
.message-field{left:217px;top:1349px;width:420px;height:108px;color:#7fcfc3;font-size:12px;padding:8px}
.btn{height:24px;border:1px solid #c7c7c7;border-radius:3px;background:linear-gradient(#fff,#e9e9e9);font-size:12px;color:#555;display:flex;align-items:center;justify-content:center}
.post-btn{left:531px;top:1474px;width:106px}

/* discussion */
.post-meta{left:141px;top:1516px;width:496px;height:30px;background:var(--teal-pale);font-size:10px;color:var(--muted);display:flex;align-items:center;justify-content:space-between;padding:0 18px}
.post-meta b{color:var(--teal);font-weight:400}
.avatar{background:linear-gradient(135deg,#d9c3b4,#8a6f63)}
.main-avatar{left:153px;top:1583px;width:60px;height:58px}
.commenter{font-size:11px;color:var(--teal);text-align:center}
.main-name{left:153px;top:1646px;width:60px;font-size:18px}
.comment-text{left:240px;top:1583px;width:400px;font-size:11px;line-height:17px;color:#444}
.view-all{left:515px;top:1677px;font-size:10px;color:var(--teal);display:flex;align-items:center;gap:5px}
.view-all span{width:16px;height:12px;border-radius:2px;background:var(--teal)}
.reply{left:222px;width:428px;height:62px}
.reply.shade{background:var(--teal-pale)}
.reply .avatar{position:absolute;left:5px;top:4px;width:40px;height:40px}
.reply .commenter{position:absolute;left:0;top:46px;width:50px;font-size:10px}
.reply p{position:absolute;left:60px;top:6px;width:360px;font-size:11px;line-height:16px;color:#444}
.reply-field{left:272px;top:1921px;width:378px;height:30px;font-size:11px;color:#7fcfc3;padding:7px 10px}
.reply-btn{left:533px;top:1968px;width:117px}

/* products */
.catalog{left:687px;top:704px;display:grid;grid-template-columns:175px 175px;column-gap:30px;grid-auto-rows:257px}
.product{position:relative}
.product h3{font-size:14px;color:var(--teal);font-weight:700}
.product dl{margin-top:8px;font-size:11px;line-height:20px;display:grid;grid-template-columns:48px 1fr;color:#444}
.product .shot{margin:6px 0 0 10px;width:150px;height:82px;border-radius:4px}
.product .btn{position:absolute;left:12px;top:168px;width:118px}
.tone-a{background:linear-gradient(120deg,#e9e2da,#8f7a6a,#d9c9b8)}
.tone-b{background:linear-gradient(120deg,#f0eef2,#3b3a55,#9a8fb6)}
.tone-c{background:linear-gradient(120deg,#f4e9ee,#c63b74,#2b2b2b)}
.tone-d{background:linear-gradient(120deg,#efe6da,#4a3a2c,#b08a5a)}
.tone-e{background:linear-gradient(120deg,#f7ece8,#c55d6c,#3a2f2f)}
.tone-f{background:linear-gradient(120deg,#fbe9e7,#1f1f1f,#e6b3a9)}
.tone-g{background:linear-gradient(120deg,#f6eee2,#e07b1a,#222)}
.tone-h{background:linear-gradient(120deg,#f4efe8,#d9b28a,#151515)}
.tone-i{background:linear-gradient(120deg,#ecebef,#2d2f4a,#8c93b5)}
.tone-j{background:linear-gradient(120deg,#f6ede4,#c99b6c,#c04a44)}

/* footer */
.footer-brand{left:869px;top:2040px;display:flex;align-items:center;gap:10px;font-family:"Open Sans",sans-serif;font-weight:700;font-size:46px;color:#222;letter-spacing:-1px}
.footer-brand span{width:18px;height:18px;border-radius:50%;background:var(--teal)}
.site-footer{left:0;top:2112px;width:1200px;height:110px;background:var(--teal);color:#fff;text-align:center}
.footer-nav{margin-top:22px;display:flex;justify-content:center;gap:28px;font-size:11px;padding-right:20px}
.copyright{margin-top:8px;font-size:9px;padding-right:20px}
</style>
</head>
<body>

<header class="abs site-header"></header>
<div class="abs brand">Glossaro<span class="brand-dot"></span></div>
<div class="abs subscribe"><span class="rss"></span><span class="lead">Please subscribe to:</span> Posts | Comments | Email</div>
<div class="abs search"></div>
<div class="abs search-btn">
  <svg width="30" height="30" viewBox="0 0 30 30"><circle cx="13" cy="13" r="5" fill="none" stroke="#fff" stroke-width="2"/><line x1="17" y1="17" x2="21" y2="21" stroke="#fff" stroke-width="2"/></svg>
</div>
<div class="abs social one"><span></span></div>
<div class="abs social two"><span></span></div>
<div class="abs social three"><span></span></div>
<div class="abs pill howto">HOW TO</div>
<div class="abs pill tips">TIPS</div>

<nav class="abs main-nav">
  <a>Home</a><a class="active">About Us</a><a>Portfolio</a><a>Other Link</a><a>Something</a><a>Whats This?</a>
</nav>

<div class="abs band"></div>
<section class="abs feature"></section>
<h1 class="abs feature-title">Sed neque ipsum pulvinar eu</h1>
<div class="abs meta">
  <span>Difficult <i></i><i></i><i class="off"></i></span>
  <span>Duration: 20 Minutes</span>
  <span>Opportunity: Some</span>
</div>
<div class="abs player">
  <div class="abs video-still" role="img" aria-label="Video still of a make-up lip tutorial"></div>
  <div class="abs play">
    <svg width="46" height="42" viewBox="0 0 46 42"><polygon points="18,12 31,21 18,30" fill="#fff"/></svg>
  </div>
  <div class="abs controls">
    <svg width="12" height="12" viewBox="0 0 12 12"><polygon points="2,1 11,6 2,11" fill="#ddd"/></svg>
    <span>00:00</span>
    <div class="track"><b></b></div>
    <span>00:20</span>
    <svg width="14" height="12" viewBox="0 0 14 12"><polygon points="1,4 4,4 8,1 8,11 4,8 1,8" fill="#ddd"/></svg>
    <svg width="40" height="10" viewBox="0 0 40 10"><rect x="0" y="3" width="4" height="5" fill="#ddd"/><rect x="7" y="3" width="4" height="5" fill="#ddd"/><rect x="14" y="3" width="4" height="5" fill="#ddd"/><rect x="21" y="3" width="4" height="5" fill="#ddd"/><rect x="28" y="3" width="4" height="5" fill="#777"/></svg>
  </div>
</div>
<p class="abs feature-copy">Sed tempor lectus in risus. Nullam vestibulum, odio ac pulvinar condimentum, urna neque aliquet ipsum, in blandit velit nunc eget mauris. Suspendisse aliquet sem ut nulla. Cras mollis ornare nisl. Morbi ac mi. Nunc eget nisl. Donec et tortor. Integer habitant morbi tristique senectus et netus et malesuada fames ac turpis egestas. <span class="more">Read more »</span></p>
<ul class="abs product-list">
  <li><span class="bullet"><svg width="18" height="18" viewBox="0 0 18 18"><polyline points="7,5 11,9 7,13" fill="none" stroke="#fff" stroke-width="2"/></svg></span><div><strong>Produit 1</strong><small>Sed neque ipsum pulvinar eu...</small></div></li>
  <li><span class="bullet"><svg width="18" height="18" viewBox="0 0 18 18"><polyline points="7,5 11,9 7,13" fill="none" stroke="#fff" stroke-width="2"/></svg></span><div><strong>Produit 2</strong><small>Cras eu eros id dui porttitor...</small></div></li>
  <li><span class="bullet"><svg width="18" height="18" viewBox="0 0 18 18"><polyline points="7,5 11,9 7,13" fill="none" stroke="#fff" stroke-width="2"/></svg></span><div><strong>Produit 3</strong><small>Vivamus vitae nibh id quam...</small></div></li>
  <li><span class="bullet"><svg width="18" height="18" viewBox="0 0 18 18"><polyline points="7,5 11,9 7,13" fill="none" stroke="#fff" stroke-width="2"/></svg></span><div><strong>Produit 4</strong><small>Aenean vulputate fermentum...</small></div></li>
</ul>

<div class="abs tab video">Video</div>
<div class="abs tab photo">Photo</div>
<section class="abs photo-panel"></section>
<div class="abs gallery-photo" role="img" aria-label="Photo of a make-up artist applying foundation to a client"></div>
<div class="abs arrow prev"><svg width="44" height="44" viewBox="0 0 44 44"><polyline points="25,14 17,22 25,30" fill="none" stroke="#fff" stroke-width="3"/></svg></div>
<div class="abs arrow next"><svg width="44" height="44" viewBox="0 0 44 44"><polyline points="19,14 27,22 19,30" fill="none" stroke="#fff" stroke-width="3"/></svg></div>
<h2 class="abs panel-title">Ut sagittis ultrices urna</h2>
<p class="abs panel-copy">Morbi condimentum tempus tincidunt. Sed neque ipsum, pulvinar eu tristique sollicitudin, tincidunt at nisl. Aenean feugiat risus sed lacus aliquam et adipiscing elit sodales. Aenean in erat sed neque convallis convallis at eu metus. In varius lacus quis diam cursus posuere fames ac turpis egestas.</p>

<h3 class="abs form-title">COMMENTS</h3>
<span class="abs label" style="top:1282px">Name</span>
<span class="abs label" style="top:1320px">Email</span>
<div class="abs field name-field"></div>
<div class="abs field email-field"></div>
<div class="abs field message-field">Type your comment here ...</div>
<div class="abs btn post-btn">Post</div>

<div class="abs post-meta"><span>Posted by <b>Amira</b> on Feb 13, 2011 in <b>Category, Some Category</b> |</span><b>20 Comments</b></div>
<div class="abs avatar main-avatar" role="img" aria-label="Commenter avatar"></div>
<div class="abs commenter main-name">Amira</div>
<p class="abs comment-text">Sed tempor lectus in risus. Nullam vestibulum, odio ac pulvinar condimentum, urna neque aliquet ipsum, in blandit velit nunc eget mauris. Suspendisse aliquet sem ut nulla. Cras mollis ornare nisl. Morbi ac mi. Nunc eget nisl. Donec et enim.</p>
<div class="abs view-all"><span></span>View all 6 Comments</div>

<div class="abs reply shade" style="top:1709px"><div class="avatar" role="img" aria-label="Commenter avatar"></div><div class="commenter">Elin</div><p>Sed tempor lectus in risus. Nullam vestibulum, odio ac pulvinar condimentum, urna neque aliquet ipsum, in blandit velit nunc eget mauris.</p></div>
<div class="abs reply" style="top:1778px"><div class="avatar" role="img" aria-label="Commenter avatar"></div><div class="commenter">Amira</div><p>Sed tempor lectus in risus. Nullam vestibulum, odio ac pulvinar condimentum, urna neque aliquet ipsum, in blandit velit nunc eget mauris.</p></div>
<div class="abs reply shade" style="top:1847px"><div class="avatar" role="img" aria-label="Commenter avatar"></div><div class="commenter">Elin</div><p>Sed tempor lectus in risus. Nullam vestibulum, odio ac pulvinar condimentum, urna neque aliquet ipsum, in blandit velit nunc eget mauris.</p></div>
<div class="abs field reply-field">write a reply...</div>
<div class="abs btn reply-btn">Reply</div>

<section class="abs catalog">
  <article class="product"><h3>Sagittis Ultrices</h3><dl><dt>Brand</dt><dd>: Lorem Ipsum</dd><dt>Price</dt><dd>: $29.00,-</dd></dl><div class="shot tone-a" role="img" aria-label="Powder brush and compact"></div><div class="btn">Buy Now!</div></article>
  <article class="product"><h3>Sagittis Ultrices</h3><dl><dt>Brand</dt><dd>: Lorem Ipsum</dd><dt>Price</dt><dd>: $29.00,-</dd></dl><div class="shot tone-b" role="img" aria-label="Eyeshadow palette"></div><div class="btn">Buy Now!</div></article>
  <article class="product"><h3>Sagittis Ultrices</h3><dl><dt>Brand</dt><dd>: Lorem Ipsum</dd><dt>Price</dt><dd>: $29.00,-</dd></dl><div class="shot tone-c" role="img" aria-label="Make-up brushes"></div><div class="btn">Buy Now!</div></article>
  <article class="product"><h3>Sagittis Ultrices</h3><dl><dt>Brand</dt><dd>: Lorem Ipsum</dd><dt>Price</dt><dd>: $29.00,-</dd></dl><div class="shot tone-d" role="img" aria-label="Loose powder jars"></div><div class="btn">Buy Now!</div></article>
  <article class="product"><h3>Sagittis Ultrices</h3><dl><dt>Brand</dt><dd>: Lorem Ipsum</dd><dt>Price</dt><dd>: $29.00,-</dd></dl><div class="shot tone-e" role="img" aria-label="Blush compact"></div><div class="btn">Buy Now!</div></article>
  <article class="product"><h3>Sagittis Ultrices</h3><dl><dt>Brand</dt><dd>: Lorem Ipsum</dd><dt>Price</dt><dd>: $29.00,-</dd></dl><div class="shot tone-f" role="img" aria-label="Pressed powder compact"></div><div class="btn">Buy Now!</div></article>
  <article class="product"><h3>Sagittis Ultrices</h3><dl><dt>Brand</dt><dd>: Lorem Ipsum</dd><dt>Price</dt><dd>: $29.00,-</dd></dl><div class="shot tone-g" role="img" aria-label="Mascara wand"></div><div class="btn">Buy Now!</div></article>
  <article class="product"><h3>Sagittis Ultrices</h3><dl><dt>Brand</dt><dd>: Lorem Ipsum</dd><dt>Price</dt><dd>: $29.00,-</dd></dl><div class="shot tone-h" role="img" aria-label="Foundation bottle and brush"></div><div class="btn">Buy Now!</div></article>
  <article class="product"><h3>Sagittis Ultrices</h3><dl><dt>Brand</dt><dd>: Lorem Ipsum</dd><dt>Price</dt><dd>: $29.00,-</dd></dl><div class="shot tone-i" role="img" aria-label="Eyeshadow compact"></div><div class="btn">Buy Now!</div></article>
  <article class="product"><h3>Sagittis Ultrices</h3><dl><dt>Brand</dt><dd>: Lorem Ipsum</dd><dt>Price</dt><dd>: $29.00,-</dd></dl><div class="shot tone-j" role="img" aria-label="Foundation tube and lipstick"></div><div class="btn">Buy Now!</div></article>
</section>

<div class="abs footer-brand">Glossaro<span></span></div>
<footer class="abs site-footer">
  <nav class="footer-nav"><span>HOME</span><span>HOW TO</span><span>CONTACT US</span><span>PRODUCT</span><span>TIPS</span><span>TUTORIAL</span></nav>
  <p class="copyright">COPYRIGHT 2011 Glossaro.com</p>
</footer>

</body>
</html>
```